Become a Mentor - For Musicians, Artists, Producers and Teachers

Here is the full creative brief:

https://files.plenwick.com/sheets/d/4kTqpLm8Wz_2RNa7Hc3Xv91Jd0Gb5YeUsQ6fNo8rTpxa/view?mode=shared

Here is the background image file: https://www.trovecrate.com/sh/83jbwtrmq5dkx2u/BBHn4k7QTf2ZpLeXX-wr9MUHe?dl=0

LOGO:
https://www.trovecrate.com/sh/k472rufmpdo9b6w/BBKLe3RtHY5J-sFQnLZw7Ggma?dl=0

```html
<!DOCTYPE html>
<html lang="en">
<head>
<meta charset="utf-8">
<title>Become a Mentor – Ad Set</title>
<link href="https://fonts.googleapis.com/css2?family=Kaushan+Script&family=Roboto+Condensed:wght@700;900&display=swap" rel="stylesheet">
<style>
  :root{
    --purple:#3d2468;
    --blue:#39a9e6;
    --orange:#f5a94b;
    --black:#050505;
    --white:#ffffff;
    --navy:#0b1a3a;
    --photo-a:#5a5650;
    --photo-b:#2c2a2a;
    --photo-c:#8a7f74;
  }
  *{margin:0;padding:0;box-sizing:border-box}
  html,body{width:1200px;height:917px;overflow:hidden;background:var(--white)}
  body{position:relative;font-family:"Roboto Condensed",Arial,sans-serif}

  .ad{position:absolute;overflow:hidden;background:var(--black)}
  .ad > *{position:absolute}
  .ad--poster{left:40px;top:45px;width:572px;height:812px}
  .ad--banner{left:634px;top:45px;width:529px;height:195px}
  .ad--square{left:634px;top:315px;width:529px;height:526px}

  .photo{background:
      radial-gradient(ellipse at 70% 35%,var(--photo-c) 0%,transparent 45%),
      linear-gradient(120deg,var(--photo-a) 0%,var(--photo-b) 60%,#1d1c1c 100%)}

  .band-purple{background:var(--purple)}
  .torn-top{clip-path:polygon(0 6%,8% 2%,15% 7%,24% 3%,33% 8%,44% 2%,55% 6%,66% 1%,76% 6%,86% 2%,100% 5%,100% 100%,0 100%)}
  .torn-left{clip-path:polygon(8% 0,100% 0,100% 100%,4% 100%,0 82%,7% 64%,2% 45%,9% 28%,3% 12%)}

  .script{font-family:"Kaushan Script",cursive;color:var(--white);line-height:1;white-space:nowrap}

  .apply{background:var(--blue);color:var(--white);font-weight:900;text-align:right;line-height:1.05;text-transform:uppercase}
  .apply span{display:block}
  .apply .now{color:var(--navy)}

  .tagline{color:var(--orange);font-weight:700;text-transform:uppercase;line-height:1.12;white-space:nowrap}
  .headline{color:var(--white);font-weight:900;text-transform:uppercase;white-space:nowrap;line-height:1;transform-origin:left bottom}
  .audience{color:var(--orange);font-weight:700;text-transform:uppercase;white-space:nowrap;line-height:1;transform-origin:left bottom}

  .contacts{list-style:none;color:var(--white);font-weight:700;text-transform:uppercase;white-space:nowrap}
  .contacts li{display:flex;align-items:center}
  .contacts svg{flex:none}

  .brand{color:var(--white);font-weight:700;text-transform:uppercase;text-align:center;line-height:1.1;display:flex;align-items:center;justify-content:center;gap:6px}
  .brand .dot{border-radius:50%;background:var(--blue);flex:none}
</style>
</head>
<body>

<!-- Portrait poster -->
<section class="ad ad--poster">
  <div class="photo" role="img" aria-label="Photo of two young musicians talking in a recording studio beside a mixing desk and monitor speakers" style="left:0;top:0;width:572px;height:340px"></div>
  <div class="band-purple torn-top" style="left:0;top:305px;width:572px;height:240px"></div>

  <p class="script" style="left:84px;top:248px;font-size:50px">Become a</p>
  <p class="script" style="left:16px;top:318px;font-size:64px">Mentor Today</p>

  <div class="apply torn-left" style="left:413px;top:300px;width:159px;height:108px;padding:14px 18px 0 0;font-size:36px">
    <span>Apply</span><span class="now">Now</span>
  </div>

  <p class="tagline" style="left:22px;top:416px;font-size:37px">Turn your skills and passion<br>for music into a career</p>

  <svg style="left:250px;top:500px" width="322" height="30" viewBox="0 0 322 30">
    <polygon points="0,22 300,4 302,10 2,28" fill="var(--white)"/>
    <polygon points="40,26 322,9 322,14 42,30" fill="var(--orange)"/>
  </svg>

  <h2 class="headline" style="left:32px;top:548px;font-size:58px;transform:rotate(-3deg)">Start your career</h2>

  <svg style="left:0;top:604px" width="430" height="40" viewBox="0 0 430 40">
    <polygon points="0,26 360,6 361,12 2,32" fill="var(--blue)"/>
    <polygon points="12,34 400,12 402,20 14,40" fill="var(--purple)"/>
  </svg>

  <p class="audience" style="left:20px;top:654px;font-size:19.5px;transform:rotate(-2.2deg)">Designed for musicians, artists, producers &amp; teachers</p>

  <ul class="contacts" style="left:20px;top:692px;font-size:13.5px">
    <li style="height:38px;gap:12px">
      <svg width="26" height="26" viewBox="0 0 26 26"><circle cx="13" cy="13" r="11.5" fill="none" stroke="var(--blue)" stroke-width="2"/><path d="M9 7l3 3-2 2c1 2 2 3 4 4l2-2 3 3-2 2c-5 0-10-5-10-10z" fill="var(--blue)"/></svg>
      Call 1300 XXX XXX
    </li>
    <li style="height:38px;gap:12px">
      <svg width="26" height="26" viewBox="0 0 26 26"><circle cx="13" cy="13" r="11.5" fill="none" stroke="var(--blue)" stroke-width="2"/><rect x="7" y="9" width="12" height="8" fill="none" stroke="var(--blue)" stroke-width="1.6"/><path d="M7 9l6 5 6-5" fill="none" stroke="var(--blue)" stroke-width="1.6"/></svg>
      youremail@meridianacademyofsound.com.au
    </li>
    <li style="height:38px;gap:12px">
      <svg width="26" height="26" viewBox="0 0 26 26"><circle cx="13" cy="13" r="11.5" fill="none" stroke="var(--blue)" stroke-width="2"/><circle cx="13" cy="13" r="6" fill="none" stroke="var(--blue)" stroke-width="1.6"/><path d="M7 13h12M13 7c-3 3-3 9 0 12M13 7c3 3 3 9 0 12" fill="none" stroke="var(--blue)" stroke-width="1.3"/></svg>
      www.meridianacademyofsound.com.au
    </li>
  </ul>

  <div class="brand" style="left:370px;top:705px;width:185px;height:80px;font-size:17px">
    <span class="dot" style="width:12px;height:12px"></span>
    <span>Meridian Academy<br>of Sound</span>
  </div>
</section>

<!-- Wide banner -->
<section class="ad ad--banner">
  <div class="photo" role="img" aria-label="Photo of two young musicians talking in a recording studio" style="left:0;top:0;width:330px;height:195px"></div>
  <div style="left:305px;top:0;width:224px;height:195px;background:var(--black);clip-path:polygon(6% 0,100% 0,100% 100%,0 100%,4% 60%,2% 30%)"></div>

  <p class="script" style="left:40px;top:96px;font-size:26px">Become a</p>
  <p class="script" style="left:6px;top:128px;font-size:34px">Mentor Today</p>

  <div class="apply torn-left" style="left:236px;top:134px;width:76px;height:56px;padding:6px 8px 0 0;font-size:20px">
    <span>Apply</span><span class="now">Now</span>
  </div>

  <svg style="left:330px;top:8px" width="199" height="14" viewBox="0 0 199 14">
    <polygon points="10,10 199,2 199,6 12,14" fill="var(--white)"/>
    <polygon points="60,8 199,4 199,7 62,11" fill="var(--orange)"/>
  </svg>
  <h2 class="headline" style="left:300px;top:22px;font-size:25px">Start your career</h2>
  <svg style="left:300px;top:52px" width="229" height="8" viewBox="0 0 229 8"><rect x="0" y="1" width="229" height="4" fill="var(--blue)"/></svg>

  <p class="tagline" style="left:320px;top:68px;font-size:13.5px;color:var(--blue)">Turn your skills and passion<br>for music into a career</p>
  <svg style="left:305px;top:100px" width="224" height="6" viewBox="0 0 224 6"><rect x="0" y="1" width="224" height="3" fill="var(--purple)"/></svg>
  <p class="tagline" style="left:320px;top:112px;font-size:11.5px;line-height:1.1">Designed for musicians, artists,<br>producers &amp; teachers</p>

  <ul class="contacts" style="left:320px;top:140px;font-size:8.5px">
    <li style="height:16px;gap:6px"><svg width="10" height="10" viewBox="0 0 26 26"><circle cx="13" cy="13" r="11" fill="none" stroke="var(--blue)" stroke-width="3"/><path d="M9 7l3 3-2 2c1 2 2 3 4 4l2-2 3 3-2 2c-5 0-10-5-10-10z" fill="var(--blue)"/></svg>Call 1300 XXX XXX</li>
    <li style="height:16px;gap:6px"><svg width="10" height="10" viewBox="0 0 26 26"><circle cx="13" cy="13" r="11" fill="none" stroke="var(--blue)" stroke-width="3"/><rect x="7" y="9" width="12" height="8" fill="none" stroke="var(--blue)" stroke-width="2"/></svg>youremail@meridianacademyofsound.com.au</li>
    <li style="height:16px;gap:6px"><svg width="10" height="10" viewBox="0 0 26 26"><circle cx="13" cy="13" r="11" fill="none" stroke="var(--blue)" stroke-width="3"/><path d="M5 13h16" stroke="var(--blue)" stroke-width="2"/></svg>www.meridianacademyofsound.com.au</li>
  </ul>
</section>

<!-- Square ad -->
<section class="ad ad--square">
  <div class="photo" role="img" aria-label="Photo of two young musicians talking in a recording studio beside a mixing desk and monitor speakers" style="left:0;top:0;width:529px;height:300px"></div>
  <div class="band-purple torn-top" style="left:0;top:262px;width:529px;height:75px"></div>
  <div style="left:0;top:330px;width:529px;height:196px;background:var(--black)"></div>

  <p class="script" style="left:96px;top:140px;font-size:40px">Become a</p>
  <p class="script" style="left:34px;top:196px;font-size:54px">Mentor Today</p>

  <div class="apply torn-left" style="left:383px;top:226px;width:146px;height:76px;padding:9px 16px 0 0;font-size:27px">
    <span>Apply</span><span class="now">Now</span>
  </div>

  <p class="tagline" style="left:15px;top:272px;font-size:20.5px">Turn your skills and passion<br>for music into a career</p>

  <svg style="left:225px;top:310px" width="304" height="24" viewBox="0 0 304 24">
    <polygon points="0,16 280,2 281,7 1,21" fill="var(--white)"/>
    <polygon points="60,20 304,8 304,12 62,24" fill="var(--orange)"/>
  </svg>

  <h2 class="headline" style="left:26px;top:346px;font-size:51px;transform:rotate(-3deg)">Start your career</h2>

  <svg style="left:0;top:396px" width="380" height="36" viewBox="0 0 380 36">
    <polygon points="0,22 330,6 331,11 2,27" fill="var(--blue)"/>
    <polygon points="10,30 365,12 367,18 12,36" fill="var(--purple)"/>
  </svg>

  <p class="audience" style="left:14px;top:442px;font-size:18.5px;transform:rotate(-2.6deg)">Designed for musicians, artists, producers &amp; teachers</p>

  <ul class="contacts" style="left:18px;top:479px;font-size:10.5px">
    <li style="height:13px;gap:7px"><svg width="10" height="10" viewBox="0 0 26 26"><circle cx="13" cy="13" r="11" fill="none" stroke="var(--blue)" stroke-width="3"/><path d="M9 7l3 3-2 2c1 2 2 3 4 4l2-2 3 3-2 2c-5 0-10-5-10-10z" fill="var(--blue)"/></svg>Call 1300 XXX XXX</li>
    <li style="height:13px;gap:7px"><svg width="10" height="10" viewBox="0 0 26 26"><circle cx="13" cy="13" r="11" fill="none" stroke="var(--blue)" stroke-width="3"/><rect x="7" y="9" width="12" height="8" fill="none" stroke="var(--blue)" stroke-width="2"/></svg>youremail@meridianacademyofsound.com.au</li>
    <li style="height:13px;gap:7px"><svg width="10" height="10" viewBox="0 0 26 26"><circle cx="13" cy="13" r="11" fill="none" stroke="var(--blue)" stroke-width="3"/><path d="M5 13h16" stroke="var(--blue)" stroke-width="2"/></svg>www.meridianacademyofsound.com.au</li>
  </ul>

  <div class="brand" style="left:405px;top:466px;width:115px;height:54px;font-size:11px">
    <span class="dot" style="width:8px;height:8px"></span>
    <span>Meridian Academy<br>of Sound</span>
  </div>
</section>

</body>
</html>
```